Business card for Real Estate Company located in Coastal area of spain

Want a business card design. Simple, professional, horizontal layout. will be 2 sided. Name of company (logo big on front). Name of agent, phone and email address. Back side will be list of general services we provide. Would like to see 2 separate concepts using the 2 separate logo treatments. One using Rich dark, bright blue as the stock color, and the other using White as the stock color.
Logo files uploaded (2 different versions) Domain (bayridgedwell48.com) Moraira-Calpe-Altea-Javea-Denia-Marina Alta Area (perhaps across the bottom of the front of card0 Petra Linde Licensed Estate Agent / Partner Petra@bayridgedwell48.com +34.681.72.40.96 Back of card should list services offered

Real Estate Sales and Investments Real Estate Rental Management Kitchen, Bathroom Reformations Complete Home Reformation Services Window and Door Replacement Landscape and Garden Management Pool and Jacuzzi Service

Target Market(s)

Real estate and construction

Industry/Entity Type

Real Estate

Contact Information for Business Card

Logo files uploaded (2 different versions) Domain (bayridgedwell48.com) Moraira-Calpe-Altea-Javea-Denia-Marina Alta Area (perhaps across the bottom of the front of card0 Petra Linde Licensed Estate Agent / Partner Petra@bayridgedwell48.com +34.681.72.40.96

Colors

Designer to choose colors to be used in the design.

Requirements
Must have
• progressive look professional
Nice to have
• Front big logo, Agent details. Back, list of services included in project description
Should not have
• Gloss finish for card

```html
<!DOCTYPE html>
<html lang="en">
<head>
<meta charset="utf-8">
<title>Bayridgedwell48 – Business Card</title>
<link rel="stylesheet" href="https://fonts.googleapis.com/css2?family=Montserrat:wght@400;500;700&display=swap">
<style>
  :root {
    --bg: #1c1c1c;
    --stock-white: #ffffff;
    --stock-blue: #4762ab;
    --brand-blue: #3f55a6;
    --brand-violet: #a466a6;
    --ink: #2b2b2b;
    --on-blue: #ffffff;
  }
  * { margin: 0; padding: 0; box-sizing: border-box; }
  html, body {
    width: 1200px; height: 1059px; overflow: hidden;
    background: var(--bg);
    font-family: "Montserrat", sans-serif;
  }
  .card {
    position: absolute;
    width: 690px; height: 392px;
    box-shadow: 0 10px 28px rgba(0,0,0,.6);
  }
  .card--front { left: 256px; top: 89px; background: var(--stock-white); }
  .card--back  { left: 254px; top: 546px; background: var(--stock-blue); }

  /* front */
  .brand-name {
    position: absolute; left: 30px; top: 177px; width: 294px; text-align: center;
    font-size: 23px; font-weight: 500; line-height: 1; color: var(--brand-blue);
  }
  .front-divider {
    position: absolute; left: 343px; top: 127px; width: 1px; height: 139px;
    background: linear-gradient(var(--brand-violet), var(--brand-blue));
  }
  .agent { position: absolute; left: 368px; top: 121px; }
  .agent__name {
    font-size: 28px; font-weight: 700; line-height: 1; letter-spacing: .5px;
    background: linear-gradient(90deg, var(--brand-blue), var(--brand-violet));
    -webkit-background-clip: text; background-clip: text; color: transparent;
  }
  .agent__title { margin-top: 4px; font-size: 17px; color: var(--ink); letter-spacing: .3px; }
  .contact-list { list-style: none; margin-top: 18px; }
  .contact-list li {
    display: flex; align-items: center; gap: 9px;
    font-size: 17px; color: var(--ink); height: 27px; letter-spacing: .3px;
  }
  .contact-list svg { width: 12px; height: 12px; flex: none; }
  .service-area {
    position: absolute; left: 0; right: 0; top: 333px; text-align: center;
    font-size: 17px; color: var(--ink); letter-spacing: .3px;
  }

  /* back */
  .back-name {
    position: absolute; left: 0; right: 0; top: 70px; text-align: center;
    font-size: 42px; font-weight: 500; line-height: 1; color: var(--on-blue);
  }
  .back-rule {
    position: absolute; left: 75px; width: 544px; top: 150px; height: 1px;
    background: var(--brand-violet);
  }
  .service-list {
    position: absolute; left: 0; right: 0; top: 172px; list-style: none; text-align: center;
  }
  .service-list li {
    font-size: 15.5px; color: var(--on-blue); height: 27px; line-height: 27px; letter-spacing: .3px;
  }
</style>
</head>
<body>
  <section class="card card--front">
    <div class="brand-name">bayridgedwell48.com</div>
    <div class="front-divider"></div>
    <div class="agent">
      <div class="agent__name">PETRA LINDE</div>
      <div class="agent__title">Licensed Estate Agent / Partner</div>
      <ul class="contact-list">
        <li>
          <svg viewBox="0 0 12 12" aria-hidden="true"><path fill="#3f55a6" d="M1 4c0-2 2-2.5 5-2.5S11 2 11 4H8.5V3h-5v1zM2.5 5h7l1 5h-9z"/></svg>
          +34.681.72.40.96
        </li>
        <li>
          <svg viewBox="0 0 12 12" aria-hidden="true"><path fill="none" stroke="#3f55a6" stroke-width="1.3" d="M1 5l5-4 5 4v6H1zM1 5l5 3.5L11 5"/></svg>
          petra@bayridgedwell48.com
        </li>
        <li>
          <svg viewBox="0 0 12 12" aria-hidden="true"><circle cx="6" cy="6" r="5.3" fill="#3f55a6"/><path fill="#fff" d="M3 3.5c1.2-.4 2 .3 1.8 1.3L3.5 6.5 2.2 5zM7 6.5l2 .5-.5 2.3-1.8.8z"/></svg>
          www.bayridgedwell48.com
        </li>
      </ul>
    </div>
    <div class="service-area">Altea-Calpe-Moraira-Javea-Denia-Marina Alta</div>
  </section>

  <section class="card card--back">
    <div class="back-name">bayridgedwell48.com</div>
    <div class="back-rule"></div>
    <ul class="service-list">
      <li>Real Estate Sales and Investments</li>
      <li>Real Estate Rental Management</li>
      <li>Kitchen, Bathroom Reformations</li>
      <li>Complete Home Reformation Services</li>
      <li>Window and Door Replacement</li>
      <li>Landscape and Garden Management</li>
      <li>Pool and Jacuzzi Service</li>
    </ul>
  </section>
</body>
</html>
```